Colorful Live Music Concert Poster for Tin Harbor

Looking for a portrait oriented "poster" promoting the band's upcoming show at Marlow Lounge on Sunday, 3/22 at 8 pm, and social version (square format for Instagram). <br/><br/>Copy:<br/>Tin Harbor<br/>with The Pale Wires<br/><br/>Marlow Lounge <br/>Sunday, March 22<br/>8 pm<br/><br/>Poster must be consistent with band's overall branding seen on www.tinharborband.example and it's Tunevault page at https://music.example.com/artist/7QxRtaWpLeNmVcz2Ks9DuB?si=381fkTsYpWmaGHeLoRqdXC <br/><br/>BUT, we wouldn't mind taking in a slightly updated direction. A good example is the cover for our recent single Glad Today, which is consistent in theme and color palette while updating the design and color at the same time. <br/><br/>The attached files include some band logo art as well as examples of posters done for prior shows. <br/><br/>The posters need not include photos of the band, but if you are so inclined, we've uploaded some selects as well.<br/><br/>Thank you. <br/><br/>Wendell<br/>Tin Harbor

```html
<!DOCTYPE html>
<html lang="en">
<head>
<meta charset="utf-8">
<title>Tin Harbor – Live at Marlow Lounge</title>
<link rel="stylesheet" href="https://fonts.googleapis.com/css2?family=Josefin+Sans:wght@300;400&family=Roboto:wght@300;400&display=swap">
<style>
  :root {
    --teal: #22a5a9;
    --navy: #1c2a5a;
    --navy-muted: #3b4a7e;
    --orange: #f7ae2b;
    --sky: #1ba3dc;
    --page: #ffffff;
  }
  * { box-sizing: border-box; margin: 0; padding: 0; }
  html, body { width: 1200px; height: 1000px; overflow: hidden; background: var(--page); }
  body { position: relative; font-family: "Roboto", Arial, sans-serif; }

  .display { font-family: "Josefin Sans", "Helvetica Neue", sans-serif; font-weight: 300; }

  /* Portrait poster */
  .poster {
    position: absolute; left: 80px; top: 93px; width: 528px; height: 815px;
    background: var(--teal);
    box-shadow: 4px 5px 8px rgba(0,0,0,.22);
  }
  .poster__photo {
    position: absolute; left: 47px; top: 59px; width: 434px; height: 541px;
    background:
      linear-gradient(180deg, rgba(255,255,255,.0) 0%, rgba(255,255,255,0) 55%, rgba(80,120,60,.35) 100%),
      linear-gradient(90deg, #6f6a5a 0%, #9aa48a 18%, #e6e4dc 40%, #d9d6cc 62%, #8fa383 82%, #5f7250 100%);
  }
  .poster__title {
    position: absolute; left: 47px; top: 59px; width: 434px; height: 200px;
  }
  .poster__title text { fill: var(--teal); }
  .poster__band {
    position: absolute; left: 0; top: 660px; width: 528px; height: 155px;
    background: var(--navy);
  }
  .poster__name {
    position: absolute; left: 47px; top: 18px;
    font-size: 28px; letter-spacing: 3px; color: var(--orange); line-height: 1;
  }
  .support { font-size: 12px; line-height: 1; }
  .support__with { color: var(--teal); }
  .support__act { color: var(--orange); }
  .poster__support { position: absolute; left: 47px; top: 53px; }
  .poster__rule {
    position: absolute; left: 47px; top: 75px; width: 112px; height: 1px;
    background: var(--orange); opacity: .7;
  }
  .poster__details { position: absolute; left: 47px; top: 89px; font-size: 12px; line-height: 17px; }
  .venue { color: var(--orange); }
  .when { color: var(--navy-muted); }
  .poster__mark {
    position: absolute; left: 356px; top: 62px; display: flex; align-items: center; gap: 8px;
  }
  .poster__mark-dot { width: 16px; height: 16px; border-radius: 50%; background: var(--teal); }
  .poster__mark-name { font-size: 22px; color: var(--orange); letter-spacing: 1px; }

  /* Square social */
  .social {
    position: absolute; left: 705px; top: 292px; width: 416px; height: 416px;
    background: var(--teal);
    box-shadow: 4px 5px 8px rgba(0,0,0,.22);
  }
  .social__photo {
    position: absolute; left: 91px; top: 91px; width: 234px; height: 234px;
    background:
      linear-gradient(90deg, #f0d6d0 0%, #e9b7b4 30%, #f3efe9 42%, #c35a26 58%, #a64b1f 70%, #5b6b78 85%, #2f4a2e 100%);
  }
  .social__dot {
    position: absolute; left: 75px; top: 76px; width: 32px; height: 32px;
    border-radius: 50%; background: var(--navy);
  }
  .social__badge {
    position: absolute; left: 256px; top: 89px; width: 68px; height: 68px;
    border-radius: 50%; background: var(--sky);
  }
  .social__name {
    position: absolute; left: 263px; top: 107px;
    font-size: 15px; letter-spacing: 1.5px; color: var(--navy); line-height: 1; white-space: nowrap;
  }
  .social__support { position: absolute; left: 263px; top: 126px; font-size: 9px; color: var(--navy); white-space: nowrap; }
  .social__support .support__with { color: var(--navy); }
  .social__support .support__act { color: var(--navy); }
  .social__event {
    position: absolute; left: 57px; top: 290px; width: 86px; height: 86px;
    border-radius: 50%; background: var(--orange);
  }
  .social__details { position: absolute; left: 80px; top: 308px; color: var(--navy); white-space: nowrap; }
  .social__venue { font-size: 17px; line-height: 20px; }
  .social__when { font-size: 12px; line-height: 16px; }
</style>
</head>
<body>

  <section class="poster">
    <div class="poster__photo" role="img" aria-label="Band portrait: two musicians seated beneath palm trees in front of a white building"></div>
    <svg class="poster__title display" viewBox="0 0 434 200" aria-label="Tin Harbor">
      <text x="45" y="82" font-size="96" textLength="330" lengthAdjust="spacing">TIN</text>
      <text x="8" y="188" font-size="96" textLength="424" lengthAdjust="spacing">HARBOR</text>
    </svg>

    <div class="poster__band">
      <h1 class="poster__name display">TIN HARBOR</h1>
      <p class="poster__support support"><span class="support__with">with</span> <span class="support__act">The Pale Wires</span></p>
      <div class="poster__rule"></div>
      <div class="poster__details">
        <p class="venue">Marlow Lounge</p>
        <p class="when">Sunday, March 22</p>
        <p class="when">8pm</p>
      </div>
      <div class="poster__mark">
        <span class="poster__mark-dot"></span>
        <span class="poster__mark-name display">Tin Harbor</span>
      </div>
    </div>
  </section>

  <section class="social">
    <div class="social__photo" role="img" aria-label="Close-up of a guitarist playing a sunburst electric guitar beside a singer in pink"></div>
    <div class="social__dot"></div>
    <div class="social__badge"></div>
    <h2 class="social__name display">TIN HARBOR</h2>
    <p class="social__support"><span class="support__with">with</span> <span class="support__act">The Pale Wires</span></p>
    <div class="social__event"></div>
    <div class="social__details">
      <p class="social__venue">Marlow Lounge</p>
      <p class="social__when">Sunday, March 22</p>
      <p class="social__when">8pm</p>
    </div>
  </section>

</body>
</html>
```